Pemberton Dialworks Business Card Design

Double Sided Business Card Design for a Locksmith company specializing in Safecracking, safe & vault service.

```html
<!DOCTYPE html>
<html lang="en">
<head>
<meta charset="utf-8">
<title>Pemberton Dialworks – Business Card</title>
<link rel="stylesheet" href="https://fonts.googleapis.com/css2?family=Montserrat:wght@300;400;700;800&display=swap">
<style>
  :root {
    --canvas: #e9e7e4;
    --card: #1f1e1f;
    --green: #1f7a3a;
    --green-soft: rgba(31, 122, 58, 0.35);
    --grey-soft: rgba(70, 70, 70, 0.55);
    --white: #ffffff;
  }
  * { box-sizing: border-box; margin: 0; padding: 0; }
  html, body {
    width: 1200px; height: 900px; overflow: hidden;
    background: var(--canvas);
    font-family: "Montserrat", Arial, sans-serif;
  }
  .canvas { position: relative; width: 1200px; height: 900px; }
  .card {
    position: absolute; left: 250px; width: 700px; height: 400px;
    background: var(--card); overflow: hidden;
    box-shadow: 0 6px 18px rgba(0,0,0,0.18);
  }
  .card--back { top: 40px; }
  .card--front { top: 470px; }

  .brand { display: flex; align-items: center; gap: 14px; }
  .brand-dot { border-radius: 50%; background: var(--green); flex: none; }
  .brand-name {
    color: var(--green); font-weight: 800; text-transform: uppercase;
    line-height: 1.05; letter-spacing: 0.04em;
  }

  /* front */
  .front-decor-top {
    position: absolute; right: 0; top: 0; width: 300px; height: 70px;
    background: linear-gradient(90deg, rgba(70,70,70,0) 0%, var(--grey-soft) 100%);
  }
  .front-decor-bottom {
    position: absolute; left: 0; bottom: 0; width: 700px; height: 150px;
    background: linear-gradient(180deg, rgba(31,122,58,0) 0%, var(--green-soft) 60%, rgba(50,50,50,0.5) 100%);
  }
  .card--front .brand {
    position: absolute; left: 50%; top: 50%;
    transform: translate(-50%, -58%);
  }
  .card--front .brand-dot { width: 86px; height: 86px; }
  .card--front .brand-name { font-size: 40px; }

  /* back */
  .back-identity {
    position: absolute; left: 48px; top: 96px; width: 290px;
  }
  .card--back .brand-dot { width: 60px; height: 60px; }
  .card--back .brand-name { font-size: 24px; }
  .person { margin-top: 38px; text-align: right; color: var(--white); }
  .person-first { font-weight: 700; font-size: 26px; }
  .person-last { font-weight: 300; font-size: 30px; letter-spacing: 0.02em; }

  .contacts {
    position: absolute; left: 390px; top: 108px; list-style: none;
  }
  .contact {
    display: flex; align-items: center; gap: 16px;
    color: var(--white); font-size: 15px; font-weight: 400;
    letter-spacing: 0.04em; height: 44px;
  }
  .contact-icon {
    width: 28px; height: 28px; border-radius: 50%;
    background: var(--green); display: flex;
    align-items: center; justify-content: center; flex: none;
  }
  .contact-icon svg { width: 15px; height: 15px; }
</style>
</head>
<body>
<div class="canvas">

  <section class="card card--back" aria-label="Card back">
    <div class="back-identity">
      <div class="brand">
        <span class="brand-dot"></span>
        <span class="brand-name">Pemberton<br>Dialworks</span>
      </div>
      <div class="person">
        <p class="person-first">Name</p>
        <p class="person-last">Last Name</p>
      </div>
    </div>
    <ul class="contacts">
      <li class="contact">
        <span class="contact-icon"><svg viewBox="0 0 24 24" fill="none" stroke="#fff" stroke-width="2" stroke-linecap="round" stroke-linejoin="round"><path d="M22 16.9v3a2 2 0 0 1-2.2 2 19.8 19.8 0 0 1-8.6-3.1 19.5 19.5 0 0 1-6-6A19.8 19.8 0 0 1 2.1 4.2 2 2 0 0 1 4.1 2h3a2 2 0 0 1 2 1.7c.1.9.4 1.8.7 2.7a2 2 0 0 1-.5 2.1L8 9.8a16 16 0 0 0 6 6l1.3-1.3a2 2 0 0 1 2.1-.4c.9.3 1.8.6 2.7.7a2 2 0 0 1 1.7 2z"/></svg></span>
        0123 456 789
      </li>
      <li class="contact">
        <span class="contact-icon"><svg viewBox="0 0 24 24" fill="none" stroke="#fff" stroke-width="2" stroke-linecap="round" stroke-linejoin="round"><path d="M12 22s7-6.2 7-12a7 7 0 0 0-14 0c0 5.8 7 12 7 12z"/><circle cx="12" cy="10" r="2.5"/></svg></span>
        Place, Place Address
      </li>
      <li class="contact">
        <span class="contact-icon"><svg viewBox="0 0 24 24" fill="none" stroke="#fff" stroke-width="2"><circle cx="12" cy="12" r="9"/><path d="M3 12h18M12 3c3 3.2 3 14.8 0 18M12 3c-3 3.2-3 14.8 0 18"/></svg></span>
        www.website.com
      </li>
      <li class="contact">
        <span class="contact-icon"><svg viewBox="0 0 24 24" fill="none" stroke="#fff" stroke-width="2" stroke-linejoin="round"><rect x="3" y="5" width="18" height="14" rx="1.5"/><path d="M3 6l9 7 9-7"/></svg></span>
        youremail@mail.com
      </li>
    </ul>
  </section>

  <section class="card card--front" aria-label="Card front">
    <div class="front-decor-top" role="img" aria-label="Decorative grey angled line pattern"></div>
    <div class="front-decor-bottom" role="img" aria-label="Decorative green and grey angled line pattern"></div>
    <div class="brand">
      <span class="brand-dot"></span>
      <span class="brand-name">Pemberton<br>Dialworks</span>
    </div>
  </section>

</div>
</body>
</html>
```